Cobalt Ridge Mini Storage - Ad for half Page

Need half page ad for a publication.
would also like to be able to use in the future
self storage facility - 3 locations, the third opening soon
do not like real busy projects...i have a logo but willing to tweak if needed

```html
<!DOCTYPE html>
<html lang="en">
<head>
<meta charset="utf-8">
<title>Cobalt Ridge Mini Storage – Coming Soon</title>
<link href="https://fonts.googleapis.com/css2?family=Exo+2:wght@300;400;700&family=Fredoka:wght@700&display=swap" rel="stylesheet">
<style>
  :root {
    --page: #ffffff;
    --kraft: #d9b792;
    --kraft-soft: #d3ae80;
    --brown: #6b3414;
    --ink: #1c1c1c;
    --ink-shadow: #a88a68;
    --divider: #b89670;
  }
  html, body {
    margin: 0;
    padding: 0;
    width: 1068px;
    height: 1200px;
    overflow: hidden;
    background: var(--page);
  }
  .canvas {
    position: relative;
    width: 1068px;
    height: 1200px;
    background: var(--page);
  }
  .ad {
    position: absolute;
    left: 243px;
    top: 164px;
    width: 587px;
    height: 880px;
    background: var(--kraft);
    font-family: "Exo 2", sans-serif;
    color: var(--ink);
    overflow: hidden;
  }
  .brand {
    position: absolute;
    left: 130px;
    top: 60px;
    display: flex;
    align-items: center;
    gap: 14px;
    color: var(--brown);
    font-family: "Exo 2", sans-serif;
    font-weight: 700;
  }
  .brand-mark {
    width: 66px;
    height: 66px;
    background: var(--brown);
  }
  .brand-name {
    font-size: 31px;
    line-height: 33px;
  }
  .unit-illustration {
    position: absolute;
    left: 214px;
    top: 184px;
    width: 156px;
    height: 153px;
    background: linear-gradient(180deg, var(--kraft-soft), var(--kraft));
  }
  .frame {
    position: absolute;
    left: 0;
    top: 0;
    width: 587px;
    height: 880px;
  }
  .headline {
    position: absolute;
    left: 0;
    top: 0;
    width: 587px;
    margin: 0;
    font-family: "Fredoka", sans-serif;
    font-weight: 700;
    color: var(--ink);
    text-shadow: 5px 5px 0 var(--ink-shadow);
  }
  .headline span {
    position: absolute;
    display: block;
    white-space: nowrap;
    letter-spacing: -7px;
    line-height: 1;
  }
  .headline-coming {
    left: 66px;
    top: 262px;
    font-size: 132px;
    transform: rotate(-12deg);
  }
  .headline-soon {
    left: 120px;
    top: 382px;
    font-size: 132px;
    transform: rotate(-9deg);
  }
  .location {
    position: absolute;
    left: 0;
    top: 546px;
    width: 587px;
    margin: 0;
    text-align: center;
    font-weight: 700;
    font-size: 33px;
    letter-spacing: 0.5px;
    color: var(--brown);
  }
  .intro {
    position: absolute;
    left: 50px;
    top: 682px;
    width: 487px;
    margin: 0;
    text-align: center;
    font-weight: 400;
    font-size: 19.5px;
    line-height: 23.5px;
  }
  .contact-rule {
    position: absolute;
    left: 63px;
    top: 822px;
    width: 460px;
    height: 1px;
    background: var(--brown);
  }
  .contacts {
    position: absolute;
    left: 70px;
    top: 841px;
    display: flex;
    align-items: flex-start;
    color: var(--ink);
  }
  .contact {
    display: flex;
    flex-direction: column;
    padding-right: 8px;
    margin-right: 8px;
    border-right: 1px solid var(--divider);
  }
  .contact:last-child { border-right: 0; margin-right: 0; }
  .contact-city {
    font-size: 13px;
    line-height: 14px;
    font-weight: 400;
    display: flex;
    align-items: center;
    gap: 2px;
  }
  .contact-phone {
    font-size: 17px;
    line-height: 18px;
    font-weight: 700;
    letter-spacing: 0.3px;
  }
  .contact-line {
    font-size: 12.5px;
    line-height: 15px;
    display: flex;
    align-items: center;
    gap: 5px;
  }
  .icon { width: 10px; height: 10px; fill: var(--ink); flex: none; }
</style>
</head>
<body>
<div class="canvas">
  <section class="ad">
    <header class="brand">
      <div class="brand-mark"></div>
      <div class="brand-name">Cobalt Ridge<br>Mini Storage</div>
    </header>

    <div class="unit-illustration" role="img" aria-label="Illustration of a storage unit with roll-up door"></div>

    <svg class="frame" viewBox="0 0 587 880" aria-hidden="true">
      <g fill="none" stroke="#6b3414" stroke-width="9">
        <polyline points="222,234.5 91.5,234.5 91.5,333"/>
        <polyline points="91.5,443 91.5,604.5 495.5,604.5 495.5,368"/>
        <polyline points="495.5,294 495.5,234.5 366,234.5"/>
      </g>
    </svg>

    <h1 class="headline">
      <span class="headline-coming">COMING</span>
      <span class="headline-soon">SOON!</span>
    </h1>

    <p class="location">LARKSPUR @ ROUTE 9</p>

    <p class="intro">We are a family-owned, premier self-storage facility offering solutions to your Personal Storage, Business Storage and RV &amp; Boat Storage needs.</p>

    <div class="contact-rule"></div>

    <footer class="contacts">
      <div class="contact">
        <span class="contact-city"><svg class="icon" viewBox="0 0 10 10"><path d="M5 0a3.5 3.5 0 0 0-3.5 3.5C1.5 6 5 10 5 10s3.5-4 3.5-6.5A3.5 3.5 0 0 0 5 0zm0 5a1.4 1.4 0 1 1 0-2.8A1.4 1.4 0 0 1 5 5z"/></svg>Alder Falls</span>
        <span class="contact-phone">555-014-3700</span>
      </div>
      <div class="contact">
        <span class="contact-city"><svg class="icon" viewBox="0 0 10 10"><path d="M5 0a3.5 3.5 0 0 0-3.5 3.5C1.5 6 5 10 5 10s3.5-4 3.5-6.5A3.5 3.5 0 0 0 5 0zm0 5a1.4 1.4 0 1 1 0-2.8A1.4 1.4 0 0 1 5 5z"/></svg>Pine Hollow</span>
        <span class="contact-phone">555-019-7741</span>
      </div>
      <div class="contact">
        <span class="contact-line"><svg class="icon" viewBox="0 0 10 10"><path d="M0 2h10v1L5 6 0 3zM0 4l5 3 5-3v4H0z"/></svg>sales@cobaltridgestorage.com</span>
        <span class="contact-line"><svg class="icon" viewBox="0 0 10 10"><circle cx="5" cy="5" r="4.3" fill="none" stroke="#1c1c1c" stroke-width="1"/><path d="M0.7 5h8.6M5 0.7c-2.2 2.5-2.2 6.1 0 8.6M5 0.7c2.2 2.5 2.2 6.1 0 8.6" fill="none" stroke="#1c1c1c" stroke-width="0.8"/></svg>www.cobaltridgestorage.com</span>
      </div>
    </footer>
  </section>
</div>
</body>
</html>
```